Orbit 582 - Kindle Book Cover

I am looking for a Kindle book cover for my book about "Orbit 582".
The Book is Titled:
Orbit 582 Ascended
Shaping Tomorrow: Paths To Unlocking Hidden Currents
Author is Dorian Welby
Here is a book description that may help you understand more about it:
Inspired by the genius of Bertram Ollinger, this comprehensive guide delves into the ancient wisdom and cutting-edge science behind the 582 method, a powerful tool for manifesting your desires. Whether you're seeking personal growth, financial success, or spiritual enlightenment, this book provides advanced techniques and methods to transform your dreams into reality.
Any questions please ask.
Thanks
Gavin

```html
<!DOCTYPE html>
<html lang="en">
<head>
<meta charset="utf-8">
<title>Orbit 582 Ascended — Book Cover</title>
<link rel="stylesheet" href="https://fonts.googleapis.com/css2?family=Bodoni+Moda:opsz,wght@6..96,500&family=Montserrat:wght@300&family=Poppins:wght@400;800&display=swap">
<style>
  :root {
    --stage: #6e56b0;
    --cover-dark: #211e2b;
    --field-violet: #5b1b8c;
    --field-indigo: #3b2e9c;
    --title-white: #ffffff;
    --title-yellow: #ffee00;
    --glow: #c33cff;
    --band-blue: #2f7ff0;
    --tagline-magenta: #e414e6;
    --body-white: #f4f2f8;
  }
  html, body {
    margin: 0;
    width: 1200px;
    height: 2400px;
    overflow: hidden;
    background: var(--stage);
  }
  .stage {
    position: relative;
    width: 1200px;
    height: 2400px;
  }
  .book-cover {
    position: absolute;
    left: 75px;
    top: 360px;
    width: 1050px;
    height: 1680px;
    box-shadow: 0 10px 40px rgba(30, 15, 70, 0.45);
  }
  .title-word { font-family: "Bodoni Moda", "Playfair Display", serif; font-weight: 500; fill: var(--title-white); }
  .title-number { font-family: "Bodoni Moda", "Playfair Display", serif; font-weight: 500; fill: var(--title-yellow); }
  .edition { font-family: "Montserrat", sans-serif; font-weight: 300; fill: var(--title-white); letter-spacing: 0.45em; }
  .tagline { font-family: "Poppins", sans-serif; font-weight: 800; fill: var(--tagline-magenta); letter-spacing: 0.38em; }
  .subtitle { font-family: "Poppins", sans-serif; font-weight: 400; fill: var(--body-white); }
  .author { font-family: "Poppins", sans-serif; font-weight: 800; fill: var(--title-yellow); letter-spacing: 0.12em; }
</style>
</head>
<body>
<main class="stage">
  <svg class="book-cover" viewBox="0 0 1050 1680" xmlns="http://www.w3.org/2000/svg" aria-labelledby="cover-title">
    <title id="cover-title">Orbit 582 Ascended by Dorian Welby</title>
    <defs>
      <linearGradient id="field-gradient" x1="0" y1="0" x2="0" y2="1">
        <stop offset="0" stop-color="var(--field-violet)"/>
        <stop offset="0.75" stop-color="var(--field-indigo)"/>
        <stop offset="1" stop-color="var(--cover-dark)"/>
      </linearGradient>
      <radialGradient id="lower-field" cx="0.5" cy="0.3" r="0.6">
        <stop offset="0" stop-color="#3a3aa8" stop-opacity="0.9"/>
        <stop offset="1" stop-color="#3a3aa8" stop-opacity="0"/>
      </radialGradient>
      <linearGradient id="band-gradient" x1="0" y1="0" x2="1" y2="0">
        <stop offset="0" stop-color="var(--band-blue)" stop-opacity="0"/>
        <stop offset="0.5" stop-color="var(--band-blue)" stop-opacity="0.95"/>
        <stop offset="1" stop-color="var(--band-blue)" stop-opacity="0"/>
      </linearGradient>
      <linearGradient id="emblem-gradient" x1="0" y1="0" x2="0" y2="1">
        <stop offset="0" stop-color="#fff14a"/>
        <stop offset="1" stop-color="#b8a600"/>
      </linearGradient>
      <filter id="title-glow" x="-20%" y="-20%" width="140%" height="140%">
        <feGaussianBlur in="SourceAlpha" stdDeviation="9" result="blur"/>
        <feFlood flood-color="#c33cff" flood-opacity="0.85"/>
        <feComposite in2="blur" operator="in" result="glow"/>
        <feMerge><feMergeNode in="glow"/><feMergeNode in="SourceGraphic"/></feMerge>
      </filter>
    </defs>

    <rect class="cover-base" width="1050" height="1680" fill="var(--cover-dark)"/>
    <rect class="pattern-field" width="1050" height="740" fill="url(#field-gradient)" role="img" aria-label="Dotted sacred-geometry pattern in violet and indigo"/>
    <rect class="pattern-field-lower" x="120" y="700" width="810" height="420" fill="url(#lower-field)" role="img" aria-label="Fading dotted indigo pattern behind the emblem"/>

    <g class="title" filter="url(#title-glow)">
      <text class="title-word" x="525" y="294" text-anchor="middle" font-size="222">Orbit</text>
      <text class="title-number" x="525" y="594" text-anchor="middle" font-size="420">582</text>
    </g>

    <rect class="edition-band" x="60" y="631" width="930" height="77" fill="url(#band-gradient)"/>
    <text class="edition" x="540" y="690" text-anchor="middle" font-size="50">ASCENDED</text>

    <polygon class="emblem" points="539,727 813,1207 265,1207" fill="url(#emblem-gradient)" opacity="0.9" role="img" aria-label="Golden all-seeing eye inside a radiant triangle with sacred geometry circles"/>

    <text class="tagline" x="525" y="1345" text-anchor="middle" font-size="37">SHAPING TOMORROW:</text>
    <text class="subtitle" x="525" y="1404" text-anchor="middle" font-size="54">Paths To</text>
    <text class="subtitle" x="525" y="1465" text-anchor="middle" font-size="54">Unlocking Hidden Currents</text>
    <text class="author" x="525" y="1567" text-anchor="middle" font-size="52">DORIAN WELBY</text>
  </svg>
</main>
</body>
</html>
```